Young, dynamic furniture company needs a new business card design

We require a new business card design for our modern furniture company which supplies furniture and appliances to the property and development market.
Tovrenfield Furnishing has become one of the leading furniture & appliance suppliers to the property market withing London. With over 10 years experience, we have increased our business to supply not only private landlords and managing agents, but also property developers, housing associations and local councils.
We offer not only a complete range of furniture which includes beds, wardrobes, dining sets and sofas, but also a high quality, full delivery and assembly service to help you with all our furnishing needs.

Target Market(s)

Private landlords, estate agents, letting agents, property management companies

Industry/Entity Type

Business

Contact Information for Business Card

Name,
Title,
Address,
Mobile,
Telephone,
Fax, Website, email address

Font styles to use
Sans Serif

Colors
3176b5
0555a3
85abd2
cfdeed

Requirements
Must have
• All the above information for each of our staff, along with our logo

```html
<!DOCTYPE html>
<html lang="en">
<head>
<meta charset="utf-8">
<title>Tovrenfield Furnishing – Business Card</title>
<link rel="stylesheet" href="https://fonts.googleapis.com/css2?family=Roboto:wght@400;700;900&family=Roboto+Condensed:wght@300;400&family=Mulish:wght@400;500;700&display=swap">
<style>
  :root {
    --band-blue: #1f6db5;
    --brand-blue: #0555a3;
    --mid-blue: #3176b5;
    --navy: #1d2f6b;
    --ink: #1b1b1b;
    --card-white: #ffffff;
    --page-bg: #e9edf2;
  }
  * { box-sizing: border-box; margin: 0; padding: 0; }
  html, body { width: 1200px; height: 741px; overflow: hidden; }
  body {
    background: var(--page-bg);
    position: relative;
    font-family: "Mulish", sans-serif;
    color: var(--ink);
  }
  .card {
    position: absolute;
    top: 230px;
    width: 494px;
    height: 282px;
    background: var(--card-white);
    text-align: center;
    box-shadow: 0 2px 6px rgba(0,0,0,0.12);
    overflow: hidden;
  }
  .card--front { left: 98px; }
  .card--back { left: 608px; }
  .card__band {
    position: absolute;
    left: 0; right: 0;
    height: 16px;
    background: var(--band-blue);
  }
  .card__band--top { top: 0; }
  .card__band--bottom { bottom: 0; }

  .brand-mark {
    position: absolute;
    left: 0; right: 0;
    display: flex;
    align-items: center;
    justify-content: center;
    gap: 10px;
    font-family: "Roboto", sans-serif;
    font-weight: 900;
    font-size: 26px;
    letter-spacing: 0.5px;
    color: var(--navy);
    text-transform: uppercase;
    line-height: 1.05;
  }
  .brand-mark__square {
    width: 22px; height: 22px;
    background: var(--mid-blue);
    flex: none;
  }
  .card--front .brand-mark { top: 100px; }
  .card--back .brand-mark { top: 78px; }

  .company-name {
    position: absolute;
    top: 181px; left: 0; right: 0;
    font-family: "Roboto Condensed", sans-serif;
    font-weight: 400;
    font-size: 18px;
    text-transform: uppercase;
    color: var(--ink);
  }
  .company-tagline {
    position: absolute;
    top: 203px; left: 0; right: 0;
    font-family: "Roboto Condensed", sans-serif;
    font-size: 10px;
    text-transform: uppercase;
    letter-spacing: 0.3px;
    color: var(--ink);
  }
  .company-web {
    position: absolute;
    top: 231px; left: 0; right: 0;
    font-family: "Mulish", sans-serif;
    font-weight: 700;
    font-size: 13px;
    color: var(--ink);
  }
  .company-web__domain { color: var(--mid-blue); }

  .person-name {
    position: absolute;
    top: 162px; left: 0; right: 0;
    font-family: "Roboto", sans-serif;
    font-weight: 700;
    font-size: 17px;
    color: var(--band-blue);
    text-transform: uppercase;
  }
  .contact-row {
    position: absolute;
    top: 201px; left: 0; right: 0;
    display: flex;
    justify-content: center;
    gap: 9px;
    font-size: 13px;
  }
  .contact-item { display: flex; align-items: center; gap: 3px; }
  .contact-icon { width: 14px; height: 14px; flex: none; }
  .contact-line {
    position: absolute;
    left: 0; right: 0;
    font-size: 13px;
  }
  .contact-line--email { top: 222px; }
  .contact-line--address { top: 243px; }
</style>
</head>
<body>

<section class="card card--front">
  <div class="card__band card__band--top"></div>
  <div class="brand-mark"><span class="brand-mark__square"></span>Tovrenfield Furnishing</div>
  <p class="company-name">Tovrenfield Furnishing</p>
  <p class="company-tagline">Trade Furniture Solutions</p>
  <p class="company-web">www.<span class="company-web__domain">tovrenfieldhome</span>.co.uk</p>
  <div class="card__band card__band--bottom"></div>
</section>

<section class="card card--back">
  <div class="card__band card__band--top"></div>
  <div class="brand-mark"><span class="brand-mark__square"></span>Tovrenfield Furnishing</div>
  <p class="person-name">Daniel Hartley</p>
  <div class="contact-row">
    <span class="contact-item">
      <svg class="contact-icon" viewBox="0 0 14 14" aria-label="Telephone">
        <rect width="14" height="14" fill="#1f6db5"/>
        <path d="M4 3 L6 3 L6.5 5.2 L5.4 6 Q6.2 7.9 8 8.7 L8.9 7.6 L11 8.2 L11 10.2 Q7.5 10.5 5.2 8.2 Q3.2 6 4 3 Z" fill="#fff"/>
      </svg>020 7946 0318
    </span>
    <span class="contact-item">
      <svg class="contact-icon" viewBox="0 0 14 14" aria-label="Fax">
        <rect width="14" height="14" fill="#1f6db5"/>
        <rect x="4.5" y="2.5" width="5" height="3" fill="#fff"/>
        <rect x="2.5" y="5.5" width="9" height="4.5" fill="#fff"/>
        <rect x="4.5" y="8.5" width="5" height="3" fill="#fff" stroke="#1f6db5" stroke-width="0.6"/>
      </svg>020 7946 0319
    </span>
    <span class="contact-item">
      <svg class="contact-icon" viewBox="0 0 14 14" aria-label="Mobile">
        <rect width="14" height="14" fill="#1f6db5"/>
        <rect x="4.5" y="2" width="5" height="10" rx="0.8" fill="#fff"/>
        <rect x="5.3" y="3.2" width="3.4" height="6" fill="#1f6db5"/>
      </svg>07700 900412
    </span>
  </div>
  <p class="contact-line contact-line--email">daniel@tovrenfieldhome.co.uk</p>
  <p class="contact-line contact-line--address">14 Elm Row, Suite 2, Camden, London NW1 8QP, UK</p>
  <div class="card__band card__band--bottom"></div>
</section>

</body>
</html>
```